Business Card Design

New Homes
Renovations/Additions
Building Maintenance
Design
Council Approvals
Estimates
Project and Construction Management

The back of the card should only contain my logo which is attached and under the logo have written velora & velora constructions.

Industry/Entity Type

Business

Contact Information for Business Card

Company Name: Velora & Velora Constructions Pty Ltd
BLD 641372
ABN: 52 907 314 286
Position: Director
Name: Tavo Rilkenbar
Tel: m. 0418276354
f. (08)83926157
veloranvelora@mailnest.example

```html
<!DOCTYPE html>
<html lang="en">
<head>
<meta charset="utf-8">
<title>Velora &amp; Velora Constructions – Business Card</title>
<link rel="stylesheet" href="https://fonts.googleapis.com/css2?family=Cinzel:wght@400;600;700&family=Jost:wght@400&display=swap">
<style>
  :root {
    --page: #ffffff;
    --card-core: #5a1a0c;
    --card-mid: #2e0e06;
    --card-edge: #000000;
    --accent-red: #e8242a;
    --ink-light: #ffffff;
    --strip: #050201;
  }
  * { margin: 0; padding: 0; box-sizing: border-box; }
  html, body {
    width: 1000px; height: 1200px; overflow: hidden;
    background: var(--page);
  }
  .canvas { position: relative; width: 1000px; height: 1200px; }

  .card { position: absolute; overflow: hidden; }
  .card-front {
    left: 114px; top: 54px; width: 796px; height: 491px;
    background: radial-gradient(ellipse 62% 70% at 50% 50%, var(--card-core) 0%, var(--card-mid) 55%, var(--card-edge) 100%);
  }
  .card-back {
    left: 116px; top: 630px; width: 798px; height: 492px;
    background: radial-gradient(ellipse 60% 65% at 50% 42%, var(--card-core) 0%, var(--card-mid) 55%, var(--card-edge) 100%);
  }

  .company-name {
    position: absolute; left: 0; right: 0; top: 53px;
    text-align: center;
    font-family: "Cinzel", serif; font-weight: 600; font-size: 23px;
    color: var(--accent-red);
    text-shadow: 0 2px 3px rgba(0,0,0,.6);
  }
  .registration {
    position: absolute; left: 0; right: 0; top: 96px;
    text-align: center;
    font-family: "Jost", sans-serif; font-size: 16px;
    color: var(--ink-light); letter-spacing: .3px;
  }

  .person {
    position: absolute; left: 0; right: 0; top: 196px;
    display: flex; align-items: center; justify-content: center; gap: 8px;
  }
  .person-rule { height: 2px; width: 205px; }
  .person-rule.left { background: linear-gradient(to right, transparent, #d9c8c0); }
  .person-rule.right { background: linear-gradient(to left, transparent, #d9c8c0); }
  .person-name {
    font-family: "Cinzel", serif; font-weight: 400; font-size: 35px;
    color: var(--ink-light); letter-spacing: 1px;
    text-shadow: 0 2px 4px rgba(0,0,0,.7);
  }

  .contacts {
    position: absolute; top: 323px; left: 64px;
    display: flex; align-items: center;
  }
  .contact { display: flex; align-items: center; gap: 15px; margin-right: 20px; }
  .contact-icon {
    width: 33px; height: 33px; background: var(--accent-red);
    display: flex; align-items: center; justify-content: center;
  }
  .contact-text {
    font-family: "Cinzel", serif; font-size: 19px; color: var(--ink-light);
    text-transform: none; font-variant: normal;
  }
  .contact-text.numeric { font-family: "Cormorant Garamond", "Times New Roman", serif; font-size: 21px; font-weight: 600; }
  .contact-text.email { font-family: "Jost", sans-serif; font-size: 18px; }

  .services {
    position: absolute; left: 0; right: 0; top: 383px; bottom: 0;
    background: var(--strip);
    border-top: 2px solid #e9e1dc;
    padding-top: 17px;
    text-align: center;
    font-family: "Cinzel", serif; font-weight: 700; font-size: 15.5px;
    color: var(--accent-red); line-height: 29px;
  }
  .services .dot {
    display: inline-block; width: 10px; height: 10px; border-radius: 50%;
    background: var(--accent-red); margin: 0 8px; vertical-align: 1px;
  }

  .brand-mark {
    position: absolute; left: 0; right: 0; top: 170px;
    text-align: center;
    font-family: "Cinzel", serif; font-weight: 600; font-size: 40px;
    color: var(--ink-light);
  }
  .brand-title {
    position: absolute; left: 0; right: 0; top: 332px;
    text-align: center;
    font-family: "Cinzel", serif; font-weight: 600; font-size: 36px;
    color: var(--ink-light); letter-spacing: .5px;
    text-shadow: 0 3px 4px rgba(0,0,0,.8);
  }
</style>
</head>
<body>
<div class="canvas">

  <section class="card card-front">
    <h1 class="company-name">Velora &amp; Velora Constructions Pty Ltd</h1>
    <p class="registration">BLD 641372 ABN: 52 907 314 286</p>

    <div class="person">
      <span class="person-rule left"></span>
      <h2 class="person-name">Tavo Rilkenbar</h2>
      <span class="person-rule right"></span>
    </div>

    <div class="contacts">
      <div class="contact">
        <span class="contact-icon">
          <svg width="22" height="22" viewBox="0 0 24 24" aria-hidden="true"><path fill="#fff" d="M6.6 10.8a15.1 15.1 0 0 0 6.6 6.6l2.2-2.2c.3-.3.7-.4 1-.2 1.1.4 2.3.6 3.6.6.6 0 1 .4 1 1V20c0 .6-.4 1-1 1A17 17 0 0 1 3 4c0-.6.4-1 1-1h3.5c.6 0 1 .4 1 1 0 1.3.2 2.5.6 3.6.1.3 0 .7-.2 1z"/></svg>
        </span>
        <span class="contact-text numeric">0418276354</span>
      </div>
      <div class="contact">
        <span class="contact-icon">
          <svg width="22" height="22" viewBox="0 0 24 24" aria-hidden="true" fill="none" stroke="#fff" stroke-width="1.6"><path d="M7 10V3h7l3 3v4"/><rect x="3" y="10" width="18" height="10" rx="1"/><path d="M6 14h3M11 14h2M15 14h3M6 17h12"/></svg>
        </span>
        <span class="contact-text numeric">(08)83926157</span>
      </div>
      <div class="contact">
        <span class="contact-icon">
          <svg width="22" height="22" viewBox="0 0 24 24" aria-hidden="true" fill="none" stroke="#fff" stroke-width="2"><circle cx="12" cy="12" r="3.6"/><path d="M15.6 9v4.2c0 1.6 2.6 1.9 3.4.4A8 8 0 1 0 15.5 19.3"/></svg>
        </span>
        <span class="contact-text email">veloranvelora@mailnest.example</span>
      </div>
    </div>

    <div class="services">
      New Homes<span class="dot"></span>Renovations/Additions<span class="dot"></span>Building Maintenance<span class="dot"></span>Design<br>
      Council Approvals<span class="dot"></span>Estimates<span class="dot"></span>Project and Construction Management
    </div>
  </section>

  <section class="card card-back">
    <div class="brand-mark">Velora &amp; Velora</div>
    <h2 class="brand-title">Velora &amp; Velora Constructions</h2>
  </section>

</div>
</body>
</html>
```